Front & Back cover design for timber flooring brochure - A4 size

I need a design for the front and back cover of an A4 sized brochure for a timber and concrete flooring company called "Grand Oak Surfaces". The front cover should include the logo (attached), and an image + tagline for each of the three products/services that they offer which are:

1. Timber Flooring
2. Concrete Grinding & Sealing
3. Floor sanding (i have attached a photo for each of these three - however feel free to use other images if you feel they are better).

The back cover should be simple, perhaps just a continuation of the colour or graphic scheme on the front with the company contact details at the bottom.

Industry/Entity Type

Flooring

Requirements
Must have
• front cover has to have the logo with an image and text of the 3 services described. You can use the images attached or your own.

```html
<!DOCTYPE html>
<html lang="en">
<head>
<meta charset="utf-8">
<title>Grand Oak Surfaces – Brochure Cover</title>
<link rel="stylesheet" href="https://fonts.googleapis.com/css2?family=Libre+Baskerville:wght@400;700&family=Gochi+Hand&display=swap">
<style>
  :root {
    --brand-brown: #8a4f10;
    --headline-gold: #e8a42a;
    --headline-shadow: #6b3a06;
    --band-brown: #9a5409;
    --col-blue: #4c62b2;
    --col-blue-light: #c3cbe8;
    --col-sand: #eeb356;
    --col-sand-light: #f8e6c4;
    --col-green: #66a05c;
    --col-green-light: #dfe9dc;
    --frame: #f4f5f6;
    --caption-blue: #1f3fa0;
    --body-text: #ffffff;
    --paper: #ffffff;
  }
  * { margin: 0; padding: 0; box-sizing: border-box; }
  html, body { width: 848px; height: 1200px; overflow: hidden; background: var(--paper); }
  .cover {
    position: relative; width: 848px; height: 1200px; overflow: hidden;
    background: var(--paper);
    font-family: "Libre Baskerville", Georgia, serif;
  }
  .brand {
    position: absolute; top: 0; left: 0; width: 848px; height: 185px;
    display: flex; align-items: center; justify-content: center; gap: 20px;
  }
  .brand-mark { width: 30px; height: 30px; background: var(--brand-brown); }
  .brand-name {
    font-weight: 700; font-size: 50px; letter-spacing: 1px;
    color: var(--brand-brown); text-transform: uppercase;
  }
  .services { position: absolute; top: 185px; left: 0; width: 848px; height: 817px; display: flex; }
  .service { position: relative; height: 100%; }
  .service--sanding { width: 279px; background: linear-gradient(to bottom, #ffffff 0%, var(--col-blue-light) 30%, var(--col-blue) 100%); }
  .service--timber  { width: 288px; background: linear-gradient(to bottom, #ffffff 0%, var(--col-sand-light) 25%, var(--col-sand) 100%); }
  .service--concrete{ width: 281px; background: linear-gradient(to bottom, #ffffff 0%, var(--col-green-light) 25%, var(--col-green) 100%); }
  .headline {
    position: absolute; top: 200px; left: 0; width: 848px; text-align: center;
    font-weight: 700; font-size: 62px; color: var(--headline-gold);
    text-shadow: 2px 2px 0 var(--headline-shadow), 3px 3px 4px rgba(0,0,0,.4);
    z-index: 2;
  }
  .snapshot {
    position: absolute; background: var(--frame); padding: 14px 14px 0;
    box-shadow: 3px 4px 8px rgba(0,0,0,.35);
  }
  .snapshot-photo { width: 100%; }
  .snapshot-caption {
    font-family: "Gochi Hand", cursive; color: var(--caption-blue);
    font-size: 32px; text-align: center; line-height: 58px;
  }
  .snapshot--sanding { left: 11px; top: 126px; width: 260px; transform: rotate(3deg); }
  .snapshot--sanding .snapshot-photo { height: 230px; background: linear-gradient(160deg, #7a2c0e, #b44f1e 45%, #d27d3e 70%, #8e3a14); }
  .snapshot--timber { left: 13px; top: 190px; width: 262px; transform: rotate(-2deg); }
  .snapshot--timber .snapshot-photo { height: 228px; background: linear-gradient(135deg, #4a2810, #8b5326 40%, #c48a52 65%, #6a3a18); }
  .snapshot--concrete { left: 14px; top: 154px; width: 262px; transform: rotate(2deg); }
  .snapshot--concrete .snapshot-photo { height: 236px; background: radial-gradient(ellipse at 45% 55%, #8a8f78, #5c6252 60%, #3f4438); }
  .service-copy {
    position: absolute; top: 513px; left: 4px; right: 4px;
    color: var(--body-text); font-size: 19.5px; line-height: 29px;
    text-align: justify; hyphens: auto;
    text-shadow: 1px 1px 2px rgba(0,0,0,.85);
  }
  .contact-band {
    position: absolute; top: 1002px; left: 0; width: 848px; height: 198px;
    background: var(--band-brown); text-align: center;
    font-weight: 700; color: var(--headline-gold);
    text-shadow: 2px 2px 0 #3e1f02, 3px 3px 4px rgba(0,0,0,.4);
  }
  .contact-cta { font-size: 60px; line-height: 1; margin-top: 4px; }
  .contact-phone { font-size: 58px; line-height: 1; margin-top: 16px; }
</style>
</head>
<body>
<main class="cover">
  <header class="brand">
    <span class="brand-mark"></span>
    <span class="brand-name">Grand Oak Surfaces</span>
  </header>

  <h1 class="headline">Let Us “FLOOR” You</h1>

  <section class="services">
    <article class="service service--sanding">
      <figure class="snapshot snapshot--sanding">
        <div class="snapshot-photo" role="img" aria-label="Photo of a freshly sanded and polished hardwood floor"></div>
        <figcaption class="snapshot-caption">Floor Sanding</figcaption>
      </figure>
      <p class="service-copy">We can restore your hardwood floors to their original beauty and value both quickly and easily. Ask about our dustless and low VOC processes.</p>
    </article>

    <article class="service service--timber">
      <figure class="snapshot snapshot--timber">
        <div class="snapshot-photo" role="img" aria-label="Grid of timber flooring samples in various wood tones"></div>
        <figcaption class="snapshot-caption">Timber Flooring</figcaption>
      </figure>
      <p class="service-copy">Our Timber Flooring line offers you every look and feel possible from renewable resource woods. Renovating your home with timber flooring will definitely set your home a cut above.</p>
    </article>

    <article class="service service--concrete">
      <figure class="snapshot snapshot--concrete">
        <div class="snapshot-photo" role="img" aria-label="Photo of a ground and sealed glossy concrete floor"></div>
        <figcaption class="snapshot-caption">Concrete Grinding</figcaption>
      </figure>
      <p class="service-copy">Nothing is easier to work on or says professionalism like a properly ground and sealed concrete floor. Concrete painting services are available as well.</p>
    </article>
  </section>

  <footer class="contact-band">
    <p class="contact-cta">Call Today</p>
    <p class="contact-phone">1-555-203-8890</p>
  </footer>
</main>
</body>
</html>
```